Website Design for a High School

School Name: Bayt Qamarin Private Schools
sub-schools:
1-Bayt Qamarin Primary School
2-Bayt Qamarin High School for Girls
3-Bayt Qamarin High School for Boys
The design should be professional and serious and below is the details of the website.
Pages: (Home, About Us, Schools, Events, Students, Gallery, Lectures, Contact Us).
A-) Home Page:
1-Animated photos banner as main
2-Marquee for the last news.
3-Welcoming block of text
4-latest news at the body of the page.
5-Calender "on the side"
6-Number of visitors "on the side"
7-Search bar
8-options to choose a school
B-) School Page:
three schools listed as drop down menu when highlighted over the Schools button in the menu
*Each school page should contain:
1-Student login area
2-Animation photos header
3-Specific news and projects
C-) Student Login page:
have a Report Card
D-) Gallery Page
have a collection of photos.
E-)Contact Page
phone numbers
emails
feedback form
F-)Other mentioned pages
with normal text and photos page look as similar to the Home page.
Required color: Purple as main and include the logo colors
Logo: is attached.
Button link to change language to Arabic.

```html
<!DOCTYPE html>
<html lang="en">
<head>
<meta charset="utf-8">
<title>Bayt Qamarin Private Schools</title>
<link href="https://fonts.googleapis.com/css2?family=Open+Sans:wght@400;600;700;800&display=swap" rel="stylesheet">
<style>
:root{
  --purple:#6b3c98;
  --purple-dark:#4f2a75;
  --purple-light:#9a73c2;
  --lavender:#ece4f4;
  --ink:#333;
  --muted:#777;
  --grey-bg:#e9e9e9;
  --footer:#2f2f35;
  --white:#fff;
}
*{margin:0;padding:0;box-sizing:border-box}
html,body{width:843px;height:1200px;overflow:hidden}
body{font-family:"Open Sans",Arial,sans-serif;color:var(--ink);background:var(--white);position:relative}

/* hero */
.hero{position:absolute;left:0;top:0;width:843px;height:343px}
.hero-photo{position:absolute;inset:0;
  background:
   radial-gradient(ellipse 190px 230px at 690px 210px,#c9a27e 0%,#8e6a55 45%,rgba(60,40,60,0) 75%),
   linear-gradient(90deg,#2b2240 0%,#3d2c55 35%,#5a3e63 60%,#7b5a5a 100%)}
.hero-shade{position:absolute;inset:0;background:linear-gradient(90deg,rgba(20,15,35,.55) 0%,rgba(20,15,35,.25) 55%,rgba(20,15,35,0) 100%)}
.logo{position:absolute;left:22px;top:14px;display:flex;align-items:center;gap:8px;color:var(--white);font-weight:800;font-size:15px;letter-spacing:.5px}
.logo-mark{width:30px;height:30px;border-radius:50%;background:var(--purple-light)}
.topline{position:absolute;right:22px;top:10px;display:flex;align-items:center;gap:10px;color:var(--white);font-size:9px}
.topline .search{width:14px;height:14px}
.main-nav{position:absolute;right:14px;top:32px;display:flex;background:var(--purple);border-radius:2px}
.main-nav a{color:var(--white);text-decoration:none;font-size:8.5px;font-weight:700;text-transform:uppercase;padding:8px 10px}
.main-nav a.active{background:var(--purple-dark)}
.hero-copy{position:absolute;left:30px;top:122px;width:440px;color:var(--white)}
.hero-copy h1{font-size:24px;line-height:1.2;font-weight:800;text-transform:uppercase}
.hero-copy p{font-size:10px;line-height:1.5;margin-top:10px;width:380px;opacity:.9}
.hero-actions{display:flex;gap:14px;margin-top:26px}
.btn{display:flex;align-items:center;gap:8px;height:30px;padding:0 16px;font-size:9px;font-weight:700;color:var(--white);text-transform:uppercase;border-radius:2px}
.btn-primary{background:var(--purple)}
.btn-outline{border:1px solid rgba(255,255,255,.8)}
.btn svg{width:11px;height:11px}

/* news strip */
.news-strip{position:absolute;left:0;top:343px;width:843px;height:120px;background:var(--white);display:flex;justify-content:center;gap:34px;padding-top:50px;border-bottom:1px solid #eee}
.strip-item{display:flex;gap:10px;width:210px}
.thumb-round{flex:none;width:48px;height:48px;border-radius:50%;background:radial-gradient(circle at 50% 40%,#c79f85,#7a5c4f)}
.strip-item h3{font-size:9px;font-weight:700;color:var(--purple);text-transform:uppercase}
.strip-item p{font-size:7.5px;line-height:1.45;color:var(--muted);margin-top:4px}

/* welcome */
.welcome{position:absolute;left:0;top:500px;width:843px;text-align:center}
.welcome h2{font-size:20px;font-weight:700;letter-spacing:.5px;color:var(--ink)}
.welcome .rule{width:60px;height:2px;background:var(--purple);margin:8px auto 16px}
.welcome p{width:600px;margin:0 auto 10px;font-size:7.5px;line-height:1.65;color:var(--muted)}

/* schools */
.schools{position:absolute;left:0;top:720px;width:843px;display:flex;justify-content:center;gap:6px}
.school{width:220px;height:86px;background:#efefef;display:flex;align-items:center;gap:12px;padding:0 16px}
.school .badge{flex:none;width:44px;height:44px;border-radius:50%;background:#bdbdbd}
.school span{font-size:9.5px;font-weight:700;text-transform:uppercase;color:#555;line-height:1.3}
.school.active{background:var(--purple);height:100px;margin-top:-7px}
.school.active span{color:var(--white)}
.school.active .badge{background:var(--purple-light)}

/* latest news */
.latest{position:absolute;left:0;top:838px;width:843px;height:310px;background:var(--grey-bg)}
.latest h2{position:absolute;left:36px;top:28px;font-size:20px;font-weight:600;color:var(--ink);text-transform:uppercase}
.latest-list{position:absolute;left:36px;top:80px;display:flex;gap:8px}
.card{width:160px;padding:10px;height:200px}
.card.active{background:#dcdcdc}
.card .thumb-round{width:64px;height:64px;margin-bottom:12px}
.card h3{font-size:8.5px;font-weight:700;text-transform:uppercase;color:var(--ink)}
.card p{font-size:7.5px;line-height:1.5;color:var(--muted);margin:4px 0 10px}
.card .more{font-size:7.5px;font-weight:700;color:var(--ink)}
.card.active .more{color:var(--purple)}

.calendar{position:absolute;left:576px;top:22px;width:232px;height:268px;background:var(--lavender)}
.cal-head{height:96px;background:var(--purple);color:var(--white);display:flex;justify-content:space-between;padding:14px 18px}
.cal-head .day{font-size:9px;line-height:1.5}
.cal-head .date{font-size:52px;font-weight:300;line-height:1}
.cal-grid{display:grid;grid-template-columns:repeat(7,1fr);row-gap:6px;padding:12px 10px;text-align:center;font-size:8px;color:#555}
.cal-grid .wd{font-weight:700;color:var(--purple)}
.cal-grid span{display:flex;align-items:center;justify-content:center;height:18px}
.cal-grid .mark{background:var(--purple);color:var(--white);border-radius:50%;width:18px;margin:0 auto}
.cal-grid .today{background:var(--purple-dark);color:var(--white);border-radius:50%;width:18px;margin:0 auto;outline:2px solid var(--purple-light)}

/* footer */
.site-footer{position:absolute;left:0;top:1148px;width:843px;height:52px;background:var(--footer);display:flex;align-items:center;justify-content:space-between;padding:0 36px;color:#aaa;font-size:8px}
.social{display:flex;gap:8px}
.social i{display:block;width:16px;height:16px;border-radius:50%;background:#55555c}
</style>
</head>
<body>

<header class="hero">
  <div class="hero-photo" role="img" aria-label="Library bookshelves with two smiling students holding books"></div>
  <div class="hero-shade"></div>

  <div class="logo"><span class="logo-mark"></span>BAYT QAMARIN SCHOOLS</div>

  <div class="topline">
    <svg width="10" height="10" viewBox="0 0 24 24" fill="#fff"><path d="M6.6 10.8a15.1 15.1 0 0 0 6.6 6.6l2.2-2.2c.3-.3.7-.4 1-.2 1.1.4 2.3.6 3.6.6.6 0 1 .4 1 1V20c0 .6-.4 1-1 1A17 17 0 0 1 3 4c0-.6.4-1 1-1h3.5c.6 0 1 .4 1 1 0 1.3.2 2.5.6 3.6.1.3 0 .7-.2 1z"/></svg>
    <span>Toll Free: +971 4 555 0188</span>
    <svg class="search" viewBox="0 0 24 24" fill="none" stroke="#fff" stroke-width="2.5"><circle cx="10" cy="10" r="6"/><path d="M15 15l6 6"/></svg>
  </div>

  <nav class="main-nav">
    <a class="active">Home</a><a>About Us</a><a>Schools</a><a>Events</a><a>Students</a><a>Gallery</a><a>Contact Us</a>
  </nav>

  <div class="hero-copy">
    <h1>Lorem ipsum dolor sit amet, consectetuer adipiscing elit</h1>
    <p>We nurture curious minds with care, discipline and a love of learning every day.</p>
    <div class="hero-actions">
      <div class="btn btn-primary"><svg viewBox="0 0 24 24" fill="none" stroke="#fff" stroke-width="3"><path d="M5 12h14M13 6l6 6-6 6"/></svg>Get started now</div>
      <div class="btn btn-outline"><svg viewBox="0 0 24 24" fill="none" stroke="#fff" stroke-width="3"><path d="M5 12h14M13 6l6 6-6 6"/></svg>About us</div>
    </div>
  </div>
</header>

<section class="news-strip">
  <article class="strip-item">
    <div class="thumb-round" role="img" aria-label="Student portrait"></div>
    <div><h3>Latest News</h3><p>Term schedules and upcoming events are now posted for all families.</p></div>
  </article>
  <article class="strip-item">
    <div class="thumb-round" role="img" aria-label="Student portrait"></div>
    <div><h3>Latest News 2</h3><p>Our science club won first place at the regional student fair.</p></div>
  </article>
  <article class="strip-item">
    <div class="thumb-round" role="img" aria-label="Student portrait"></div>
    <div><h3>Latest News 3</h3><p>Registration for the new academic year opens on the first of April.</p></div>
  </article>
</section>

<section class="welcome">
  <h2>WELCOME</h2>
  <div class="rule"></div>
  <p>Bayt Qamarin Private Schools welcome every learner into a calm, well organised community where teachers guide each child with patience, high standards and genuine care. Our classrooms blend strong academic foundations with language, faith, arts and sport, so that students grow in knowledge, character and confidence throughout every stage of their school years.</p>
  <p>Parents are partners in this journey. Regular meetings, clear reports and an open door policy keep families informed about progress, events and opportunities. Our three campuses share one vision while giving primary pupils, young women and young men the focused attention and facilities each group deserves.</p>
  <p>Our doors are open to every family seeking a caring, rigorous and joyful education.</p>
</section>

<section class="schools">
  <div class="school"><span class="badge"></span><span>Bayt Qamarin Primary School</span></div>
  <div class="school active"><span class="badge"></span><span>Bayt Qamarin High School for Girls</span></div>
  <div class="school"><span class="badge"></span><span>Bayt Qamarin High School for Boys</span></div>
</section>

<section class="latest">
  <h2>Latest News</h2>
  <div class="latest-list">
    <article class="card">
      <div class="thumb-round" role="img" aria-label="Students at a science fair"></div>
      <h3>Latest News</h3>
      <p>Students shared projects at the spring science fair this week.</p>
      <span class="more">Read More</span>
    </article>
    <article class="card active">
      <div class="thumb-round" role="img" aria-label="Debate team students"></div>
      <h3>Latest News</h3>
      <p>Our girls' debate team reached the national finals this month.</p>
      <span class="more">Read More</span>
    </article>
    <article class="card">
      <div class="thumb-round" role="img" aria-label="Young reader with books"></div>
      <h3>Latest News</h3>
      <p>New library books arrived for primary readers ahead of term.</p>
      <span class="more">Read More</span>
    </article>
  </div>

  <aside class="calendar">
    <div class="cal-head">
      <div class="day">Friday<br>March 2014</div>
      <div class="date">28</div>
    </div>
    <div class="cal-grid">
      <span class="wd">S</span><span class="wd">M</span><span class="wd">T</span><span class="wd">W</span><span class="wd">T</span><span class="wd">F</span><span class="wd">S</span>
      <span></span><span></span><span></span><span></span><span></span><span></span><span>1</span>
      <span>2</span><span>3</span><span class="mark">4</span><span>5</span><span>6</span><span>7</span><span>8</span>
      <span>9</span><span>10</span><span>11</span><span class="mark">12</span><span>13</span><span>14</span><span>15</span>
      <span>16</span><span>17</span><span>18</span><span>19</span><span class="mark">20</span><span>21</span><span>22</span>
      <span>23</span><span>24</span><span>25</span><span>26</span><span>27</span><span class="today">28</span><span>29</span>
      <span>30</span><span>31</span><span></span><span></span><span></span><span></span><span></span>
    </div>
  </aside>
</section>

<footer class="site-footer">
  <span>© 2014 Bayt Qamarin Private Schools. All rights reserved.</span>
  <div class="social"><i></i><i></i><i></i></div>
</footer>

</body>
</html>
```